Attention Getting Doorhanger Postcard Campaign offering HUGE Rebate on New Construction Homes

I am reestablishing my real estate career in the far North Dallas, TX area and want to offer a rebate on new construction homes to help get me started. I am requesting a doorhanger as my first project but would like a theme that I can carry over to other projects including postcards and other marketing items. I want it to look high end, clean, professional and classy. I am attaching a copy of a flier that I created that needs (no graphic designer here) some prettying up. But this is just to give you an idea of the type of style that is of interest to me.

Target Market(s)

Home buyers for new construction in far north dallas suburbs. Usually a move up buyer.

Industry/Entity Type

Real Estate

Colors

Designer to choose colors to be used in the design.

Requirements
Must have
• Catch phrase, draw attention, classy clean lines, current trend colors of blues and grays. My information, Marston Pryce logo, equal housing and realtor logos. Fine Print: Not intended to solicit homes already listed for sale or buyers already in a buyers agency agreement with another brokerage. Please include offer details as listed in my flier. Again I am interested in a door hanger and the next round would be a flier or postcard.
Nice to have
• Picture of new homes that are in line with what is being built in my area. A few home builders sites: Coastal Beacon, Riverbend Homes, Fenwick Homes, Calloway Homes.

```html
<!DOCTYPE html>
<html lang="en">
<head>
<meta charset="utf-8">
<title>New Construction Rebate Door Hanger</title>
<link href="https://fonts.googleapis.com/css2?family=Jost:wght@400;500;600&display=swap" rel="stylesheet">
<style>
:root{
  --bg:#d6d6d6;
  --card-gray:#4b4b4d;
  --card-gray-dark:#3a3a3c;
  --blue:#2f7fcb;
  --blue-deep:#1f66b0;
  --navy:#1d2f55;
  --yellow:#f6e82a;
  --white:#ffffff;
  --ink:#1e1e1e;
  --strip:#555558;
}
*{margin:0;padding:0;box-sizing:border-box}
html,body{width:1200px;height:1200px;overflow:hidden;background:var(--bg)}
body{font-family:"Jost",sans-serif;color:var(--white)}
.stage{position:relative;width:1400px;height:1400px;transform:scale(0.857143);transform-origin:0 0}
.hanger{position:absolute;top:72px;width:574px;height:1206px;overflow:hidden;
  background:linear-gradient(180deg,#59595c 0%,var(--card-gray) 45%,var(--card-gray-dark) 100%)}
.hanger--front{left:98px}
.hanger--back{left:726px}
.backdrop-photo{position:absolute;left:0;top:0;width:574px;height:640px;
  background:radial-gradient(ellipse at 50% 45%,rgba(120,120,125,.35),rgba(60,60,62,0) 70%)}
.top-panel{position:absolute;top:0;background:linear-gradient(180deg,#3388d3,var(--blue) 60%,#2b78c2);
  border:1.5px solid rgba(255,255,255,.75);border-top:none}
.hanger--front .top-panel{left:52px;width:466px;height:400px}
.hanger--back .top-panel{left:50px;width:474px;height:388px}
.hang-hole{position:absolute;left:0;top:0}
.p{position:absolute;white-space:nowrap}
.yellow{color:var(--yellow)}
.awe{left:155px;top:210px;font-size:48px;font-weight:600;color:var(--yellow);letter-spacing:-1px}
.and-then{left:268px;top:214px;font-size:19px;font-weight:500;color:var(--yellow)}
.some{left:264px;top:230px;font-size:46px;font-weight:600;color:var(--yellow);letter-spacing:-1px}
.offer{left:0;width:466px;text-align:center;font-size:26px;font-weight:500;line-height:32px}
.savings{left:68px;width:444px}
.savings-head{top:418px;font-size:38px;font-weight:500;color:var(--yellow)}
.savings-body{top:462px;font-size:31px;font-weight:400;line-height:37.5px;text-align:justify;text-align-last:left;white-space:normal}
.savings-tail{top:572px;font-size:36px;font-weight:500;color:var(--yellow)}
.example-band{position:absolute;left:0;top:643px;width:574px;height:143px;
  background:linear-gradient(180deg,#2a2a2a,#0e0e0e 40%,#151515)}
.example-band .p{left:0;width:574px;text-align:center}
.ex-head{top:12px;font-size:34px;font-weight:600}
.ex-line{font-size:24px;font-weight:400}
.fine{left:auto!important;right:44px;width:auto!important;top:116px;font-size:12px}
.how-band{position:absolute;left:0;top:786px;width:574px;height:254px;
  background:linear-gradient(160deg,#3a8ad6,var(--blue) 45%,var(--blue-deep))}
.how-head{left:37px;top:22px;font-size:32px;font-weight:600}
.steps{position:absolute;left:37px;top:72px;list-style:none}
.steps li{position:relative;padding-left:33px;font-size:30px;line-height:39.5px;font-weight:400}
.steps li::before{content:"";position:absolute;left:2px;top:15px;width:14px;height:14px;border-radius:50%;background:var(--navy)}
.footer{position:absolute;left:0;top:1040px;width:574px;height:150px;background:var(--white);color:var(--ink)}
.footer-strip{position:absolute;left:0;top:1190px;width:574px;height:16px;background:var(--strip)}
.agent{position:absolute;left:40px;top:10px;font-size:18px;line-height:21px}
.agent-name{font-size:21px;font-weight:500}
.brokerage{position:absolute;left:40px;top:106px;display:flex;align-items:center;gap:6px;font-size:15px;font-weight:600;color:#3a3a3c}
.brokerage i{display:block;width:10px;height:10px;background:#3a3a3c}
.headshot-arc{position:absolute;right:26px;top:-22px;width:186px;height:186px;border-radius:50%;background:var(--white)}
.headshot{position:absolute;right:48px;top:-8px;width:164px;height:164px;border-radius:50%;
  background:radial-gradient(circle at 55% 40%,#b08a6e,#5a3a2a 60%,#2a2020)}
.bio{left:69px;top:214px;width:434px;font-size:23px;line-height:26.3px;text-align:justify;white-space:normal}
.sign{right:120px;top:348px;font-size:22px;font-weight:600;color:var(--yellow)}
.facts{position:absolute;left:70px;top:408px;width:452px;list-style:none}
.facts li{position:relative;font-size:19.5px;line-height:23px;text-align:justify;margin-bottom:23px}
.facts li::before{content:"";position:absolute;left:-30px;top:8px;width:9px;height:9px;border-radius:50%;background:var(--white)}
.home-photo{position:absolute;left:0;top:752px;width:574px;height:288px;
  background:linear-gradient(180deg,#c9b48f 0%,#a98b6a 40%,#7a6450 62%,#4f6d35 80%,#3f5a2b 100%)}
</style>
</head>
<body>
<div class="stage">

  <section class="hanger hanger--front">
    <div class="backdrop-photo" role="img" aria-label="Faded photo of a new brick home behind the panel"></div>
    <div class="top-panel">
      <svg class="hang-hole" width="466" height="200" viewBox="0 0 466 200">
        <line x1="145" y1="0" x2="172" y2="44" stroke="#1a2a44" stroke-width="1.5"/>
        <circle cx="231" cy="111" r="90" fill="none" stroke="#fff" stroke-width="1.5"/>
        <circle cx="231" cy="111" r="76" fill="#fff"/>
      </svg>
      <div class="p awe">AWE</div>
      <div class="p and-then">and then</div>
      <div class="p some">SOME</div>
      <div class="p offer" style="top:292px">Receive A minimum of <span class="yellow" style="font-size:30px">2.5%</span></div>
      <div class="p offer" style="top:324px">or more to put towards your</div>
      <div class="p offer" style="top:358px"><span class="yellow">NEW CONSTRUCTION</span> home!</div>
    </div>

    <div class="p savings savings-head">Maximize Your Savings!</div>
    <div class="p savings savings-body">My Buy &amp; List package offers a FLAT FEE on the sale of your current home.</div>
    <div class="p savings savings-tail">Saving you THOUSANDS!</div>

    <div class="example-band">
      <div class="p ex-head">For Example:</div>
      <div class="p ex-line" style="top:54px">$400,000 equals a $10,000 rebate!</div>
      <div class="p ex-line" style="top:83px">$500,000 equals a $12,500 rebate!</div>
      <div class="p fine">*Lender approval required.</div>
    </div>

    <div class="how-band">
      <div class="p how-head">HOW IT WORKS:</div>
      <ul class="steps">
        <li>Contact Dana to register</li>
        <li>Find your New Home</li>
        <li>Sign your Contract</li>
        <li>Close and Receive your REBATE!</li>
      </ul>
    </div>

    <div class="footer">
      <div class="headshot-arc"></div>
      <div class="headshot" role="img" aria-label="Portrait photo of the agent"></div>
      <div class="agent">
        <div class="agent-name">DANA WHITCOMBE</div>
        <div>REALTOR®, CRS, ABR, CNHS, CHMS</div>
        <div>Mobile: 469.555.0187</div>
        <div>Email:&nbsp; dana.whitcombe@mailbox.com</div>
      </div>
      <div class="brokerage"><i></i>Marston Pryce</div>
    </div>
    <div class="footer-strip"></div>
  </section>

  <section class="hanger hanger--back">
    <div class="backdrop-photo" role="img" aria-label="Faded photo of a new brick home behind the panel"></div>
    <div class="top-panel">
      <svg class="hang-hole" width="474" height="200" viewBox="0 0 474 200">
        <line x1="325" y1="0" x2="296" y2="42" stroke="#1a2a44" stroke-width="1.5"/>
        <circle cx="234" cy="111" r="91" fill="none" stroke="#fff" stroke-width="1.5"/>
        <circle cx="234" cy="111" r="76" fill="#fff"/>
      </svg>
    </div>
    <div class="p bio">I’ve sold hundreds of homes in the North Dallas area over the last 13 years, specializing in new construction homes. I would love to help you make your new home dreams a reality.</div>
    <div class="p sign">DANA</div>

    <ul class="facts">
      <li>We work with 100’s of builders in the local area so you are not limited to a few “select” builders.</li>
      <li>Homebuilders have the same bottom line sales price whether you have a REALTOR® representing you or not.</li>
      <li>Rebate program will not affect the price you pay for your home. Brokerage fees are paid through a separate marketing fund, not from the sales price of your home.</li>
      <li>Rebate program is in ADDITION to any builder or lender incentives.</li>
    </ul>

    <div class="home-photo" role="img" aria-label="Photo of a two-story stone and brick new construction home at sunset with a front lawn"></div>

    <div class="footer">
      <div class="headshot-arc"></div>
      <div class="headshot" role="img" aria-label="Portrait photo of the agent"></div>
      <div class="agent">
        <div class="agent-name">DANA WHITCOMBE</div>
        <div>REALTOR®, CRS, ABR, CNHS, CHMS</div>
        <div>Mobile: 469.555.0187</div>
        <div>Email:&nbsp; dana.whitcombe@mailbox.com</div>
      </div>
      <div class="brokerage"><i></i>Marston Pryce</div>
    </div>
    <div class="footer-strip"></div>
  </section>

</div>
</body>
</html>
```